RM Skyline Imaging Web Site design

I am looking for a responsive single page website deign for rmskylineimages.com. This is a drone based aerial photography and cinematography business. It should have an about us section, a services section that contains photograph service, Video footage, and Aerial mapping all under the services section, a pricing section, and then a contact page for customers to contact us.

Coding

Coded - Design and coding required

Number of Pages Required

1 page

Font styles to use
Sans Serif

Colors

Designer to choose colors to be used in the design.

Requirements
Must have
• Responsive design. About us section, services section, pricing section under the services links, and contact us section, that links to a submission page where they can send Name, address, email, and comments on what they are interested in.
• See hoverlens7.com - looking for similar design.
Should not have
• clutter, or too busy design

```html
<!DOCTYPE html>
<html lang="en">
<head>
<meta charset="utf-8">
<title>RM Skyline Imaging</title>
<link href="https://fonts.googleapis.com/css2?family=Raleway:wght@400;500;600&family=Lato:wght@400;700&display=swap" rel="stylesheet">
<style>
:root{
  --orange:#f39a1e;
  --ink:#2b2b2b;
  --body:#666;
  --white:#fff;
  --footer:#3b3b3b;
  --footer-deep:#2c2c2c;
  --player:#1c1c1c;
  --progress:#c8171b;
}
*{margin:0;padding:0;box-sizing:border-box}
html,body{width:1200px;height:4147px;overflow:hidden}
body{position:relative;background:var(--white);font-family:"Lato",sans-serif;color:var(--body)}
.abs{position:absolute}
h1,h2,h3,.nav,.brand{font-family:"Raleway",sans-serif}

/* header */
.site-header{left:0;top:0;width:1200px;height:83px;background:var(--white)}
.brand{left:160px;top:44px;font-size:17px;letter-spacing:6px;color:var(--ink);font-weight:500}
.brand-dot{left:290px;top:8px;width:30px;height:30px;border-radius:50%;background:var(--orange)}
.nav{left:0;top:0;width:1200px;height:83px;font-size:14px;font-weight:500;color:var(--ink)}
.nav a{position:absolute;top:52px;color:var(--ink);text-decoration:none}
.nav a.current{color:var(--orange)}
.nav .current-bar{position:absolute;left:600px;top:44px;width:42px;height:2px;background:var(--orange)}
.nav .sep{position:absolute;top:50px;width:1px;height:20px;background:#ddd}

/* hero */
.hero{left:0;top:83px;width:1200px;height:506px;background:linear-gradient(160deg,#5f6b78 0%,#3f4852 45%,#6c655a 100%)}
.hero-title{left:0;top:308px;width:1200px;text-align:center;color:var(--white);font-size:38px;font-weight:500;line-height:44px}
.btn-primary{left:525px;top:412px;width:144px;height:44px;background:var(--orange);color:#111;font-family:"Raleway",sans-serif;font-size:21px;font-weight:500;line-height:44px;text-align:center;border-radius:2px}

/* section titles */
.section-title{left:0;width:1200px;text-align:center;font-size:36px;font-weight:500;color:var(--ink)}
.section-title em{font-style:normal;color:var(--orange)}
.title-rule{left:560px;width:80px;height:2px;background:var(--orange)}
.title-rule::after{content:"";position:absolute;left:34px;top:-4px;width:12px;height:10px;background:var(--orange);border-radius:2px}
.on-dark{color:var(--white)}

.copy{font-size:12.5px;line-height:19px;text-align:center;color:var(--body)}

/* video player */
.player{background:var(--player);border-radius:8px;overflow:hidden}
.player .screen{position:absolute;left:0;top:0;right:0}
.player .bar{position:absolute;left:0;right:0;bottom:0;background:linear-gradient(#2a2a2a,#111)}
.play-big{position:absolute;background:#0b0b0b;border-radius:10px}

/* services */
.services{left:0;top:1535px;width:1200px;height:575px;background:linear-gradient(180deg,#3c4a58 0%,#27333e 55%,#4a5560 100%)}
.service-icon{width:110px;height:110px;border-radius:50%;background:var(--white);border:5px solid #111}
.service-name{width:300px;text-align:center;color:var(--white);font-family:"Raleway",sans-serif;font-size:20px;font-weight:500}
.service-copy{width:260px;text-align:center;color:#e6e6e6;font-size:12.5px;line-height:19px}

.thumb-caption{font-size:12.5px;line-height:18px;color:var(--ink)}

/* pilots */
.pilot-photo{border-radius:50%;background:linear-gradient(160deg,#b9c7d4,#7f93a6);border:8px solid var(--orange)}
.pilot-name{font-family:"Raleway",sans-serif;font-size:17px;color:var(--ink);font-weight:600}
.pilot-name span{font-weight:400;color:var(--body);font-size:14px}
.avatar{width:72px;height:72px;border-radius:50%;background:linear-gradient(160deg,#c9d2da,#8798a8);border:3px solid #e4e4e4}
.avatar-label{width:110px;text-align:center;font-size:11px;line-height:14px;color:var(--ink)}

/* call to action */
.cta{left:0;top:3658px;width:1200px;height:149px;background:var(--orange)}
.cta-text{left:185px;top:3712px;font-family:"Raleway",sans-serif;font-size:29px;color:var(--white)}
.btn-dark{left:894px;top:3710px;width:106px;height:38px;background:#222;color:var(--white);font-size:16px;line-height:38px;text-align:center;font-family:"Raleway",sans-serif;font-weight:500}

/* footer */
.site-footer{left:0;top:3807px;width:1200px;height:340px;background:var(--footer)}
.inquiry-panel{left:171px;top:3807px;width:272px;height:340px;background:var(--footer-deep)}
.footer-title{font-family:"Raleway",sans-serif;color:var(--white);font-size:16px}
.footer-title.large{font-size:23px}
.footer-rule{height:1px;background:#666}
.field{left:191px;width:232px;height:26px;background:#4b4b4b;color:#ddd;font-size:11px;line-height:26px;padding-left:8px}
.btn-submit{left:191px;top:4088px;width:88px;height:26px;background:var(--white);color:#222;font-size:13px;line-height:26px;text-align:center}
.links{left:500px;top:3947px;font-size:12px;line-height:21px;color:#e0e0e0}
.contact-line{font-size:12px;line-height:17px;color:#ddd}
.contact-line strong{color:var(--white)}
.footer-brand{left:720px;top:4020px;width:280px;text-align:center;font-family:"Raleway",sans-serif;color:var(--white);font-size:17px;letter-spacing:6px}
.copyright{left:500px;top:4100px;font-size:11.5px;color:#ddd}
</style>
</head>
<body>

<header class="abs site-header">
  <div class="abs brand-dot"></div>
  <div class="abs brand">RM Skyline Imaging</div>
  <nav class="abs nav">
    <span class="current-bar"></span>
    <a class="current" style="left:603px">Home</a>
    <span class="sep" style="left:672px"></span>
    <a style="left:686px">About Us</a>
    <span class="sep" style="left:768px"></span>
    <a style="left:786px">Services</a>
    <span class="sep" style="left:866px"></span>
    <a style="left:885px">Pricing</a>
    <span class="sep" style="left:952px"></span>
    <a style="left:973px">Contact Us</a>
  </nav>
</header>

<section class="abs hero" role="img" aria-label="Photo of people on a city street watching a camera drone fly overhead"></section>
<h1 class="abs hero-title" style="top:308px">We Are In A Drone Based<br>Aerial Photography And Cinematography Business</h1>
<div class="abs btn-primary">Learn More</div>

<!-- About -->
<h2 class="abs section-title" style="top:622px"><em>About RM</em> Skyline Imaging</h2>
<div class="abs title-rule" style="top:676px"></div>
<p class="abs copy" style="left:183px;top:708px;width:834px">Lorem ipsum dolor sit amet, consectetuer adipiscing elit, sed diam nonummy nibh euismod tincidunt ut laoreet dolore magna aliquam erat volutpat. Ut wisi enim ad minim veniam, quis nostrud exerci tation ullamcorper suscipit lobortis nisl ut aliquip ex ea commodo consequat. Duis autem vel eum iriure dolor in hendrerit in vulputate velit esse molestie consequat, vel illum dolore eu feugiat nulla facilisis at vero eros et accumsan et iusto odio dignissim qui blandit praesent luptatum zzril delenit augue duis dolore te feugait nulla facilisi.</p>
<p class="abs copy" style="left:183px;top:790px;width:834px">Lorem ipsum dolor sit amet, consectetuer adipiscing elit, sed diam nonummy nibh euismod tincidunt ut laoreet dolore magna aliquam erat volutpat. Ut wisi enim ad minim veniam, quis nostrud exerci tation ullamcorper suscipit lobortis nisl ut aliquip ex ea commodo consequat. Duis autem vel eum iriure dolor in hendrerit in vulputate velit esse molestie consequat, vel illum dolore eu feugiat nulla facilisis at vero eros et accumsan et iusto odio dignissim qui blandit praesent luptatum zzril delenit augue duis dolore te feugait nulla facilisi.</p>

<div class="abs player" style="left:174px;top:893px;width:852px;height:578px">
  <div class="screen" style="height:490px;background:linear-gradient(180deg,#6d7d58 0%,#4e6a3a 50%,#7aa04a 100%)" role="img" aria-label="Video still of a couple in a park with a drone hovering nearby"></div>
  <div class="play-big" style="left:386px;top:246px;width:80px;height:62px">
    <svg width="80" height="62"><polygon points="31,17 31,45 54,31" fill="#fff"/></svg>
  </div>
  <div class="bar" style="height:88px">
    <svg width="852" height="88">
      <polygon points="34,28 34,60 58,44" fill="#fff"/>
      <polygon points="108,38 116,38 126,30 126,58 116,50 108,50" fill="#fff"/>
      <path d="M131 37 q6 7 0 14 M136 33 q10 11 0 22" stroke="#fff" stroke-width="2" fill="none"/>
      <rect x="162" y="40" width="430" height="9" rx="4" fill="#444"/>
      <rect x="162" y="40" width="215" height="9" rx="4" fill="var(--progress)"/>
      <path d="M786 32 h10 M786 32 v10 M786 32 l12 12 M812 56 h-10 M812 56 v-10 M812 56 l-12 -12" stroke="#fff" stroke-width="3" fill="none"/>
    </svg>
  </div>
</div>

<!-- Services -->
<section class="abs services" role="img" aria-label="Aerial photo of a city skyline at dusk"></section>
<h2 class="abs section-title on-dark" style="top:1594px"><em>Our</em> Services</h2>
<div class="abs title-rule" style="top:1648px"></div>

<div class="abs service-icon" style="left:241px;top:1720px">
  <svg width="100" height="100"><rect x="26" y="36" width="48" height="34" rx="5" fill="#111"/><rect x="40" y="29" width="20" height="9" rx="2" fill="#111"/><circle cx="50" cy="53" r="11" fill="#fff"/><circle cx="50" cy="53" r="6" fill="#111"/></svg>
</div>
<div class="abs service-icon" style="left:545px;top:1720px">
  <svg width="100" height="100"><rect x="26" y="32" width="48" height="38" fill="#111"/><rect x="34" y="38" width="32" height="26" fill="#fff"/><g fill="#fff"><rect x="28" y="35" width="4" height="4"/><rect x="28" y="49" width="4" height="4"/><rect x="28" y="63" width="4" height="4"/><rect x="68" y="35" width="4" height="4"/><rect x="68" y="49" width="4" height="4"/><rect x="68" y="63" width="4" height="4"/></g></svg>
</div>
<div class="abs service-icon" style="left:849px;top:1720px">
  <svg width="100" height="100"><g stroke="#111" stroke-width="4"><line x1="28" y1="40" x2="72" y2="40"/></g><g fill="#111"><rect x="18" y="34" width="22" height="4" rx="2"/><rect x="60" y="34" width="22" height="4" rx="2"/><rect x="38" y="40" width="24" height="16" rx="4"/><circle cx="50" cy="62" r="6"/><rect x="32" y="56" width="3" height="12"/><rect x="65" y="56" width="3" height="12"/></g></svg>
</div>

<h3 class="abs service-name" style="left:146px;top:1870px">Photograph Service</h3>
<h3 class="abs service-name" style="left:450px;top:1870px">Video Footage</h3>
<h3 class="abs service-name" style="left:754px;top:1870px">Aerial Mapping</h3>
<p class="abs service-copy" style="left:166px;top:1916px">Lorem ipsum dolor sit amet, consectetuer adipiscing elit, sed diam nonummy nibh euismod tincidunt ut laoreet dolore magna aliquam erat volutpat. Ut wisi enim ad minim veniam, quis nostrud exerci tation ullamcorper.</p>
<p class="abs service-copy" style="left:470px;top:1916px">Lorem ipsum dolor sit amet, consectetuer adipiscing elit, sed diam nonummy nibh euismod tincidunt ut laoreet dolore magna aliquam erat volutpat. Ut wisi enim ad minim veniam, quis nostrud exerci tation ullamcorper.</p>
<p class="abs service-copy" style="left:774px;top:1916px">Lorem ipsum dolor sit amet, consectetuer adipiscing elit, sed diam nonummy nibh euismod tincidunt ut laoreet dolore magna aliquam erat volutpat. Ut wisi enim ad minim veniam, quis nostrud exerci tation ullamcorper.</p>

<!-- Recent work -->
<h2 class="abs section-title" style="top:2140px"><em>Recent</em> Work</h2>
<div class="abs title-rule" style="top:2194px"></div>

<div class="abs player" style="left:174px;top:2237px;width:852px;height:578px">
  <div class="screen" style="height:490px;background:linear-gradient(180deg,#8fb4d8 0%,#8e9aa0 35%,#6c7f4c 70%,#5c7a3c 100%)" role="img" aria-label="Video still of a large house seen from above with a drone in flight"></div>
  <div class="play-big" style="left:386px;top:246px;width:80px;height:62px">
    <svg width="80" height="62"><polygon points="31,17 31,45 54,31" fill="#fff"/></svg>
  </div>
  <div class="bar" style="height:88px">
    <svg width="852" height="88">
      <polygon points="34,28 34,60 58,44" fill="#fff"/>
      <polygon points="108,38 116,38 126,30 126,58 116,50 108,50" fill="#fff"/>
      <path d="M131 37 q6 7 0 14 M136 33 q10 11 0 22" stroke="#fff" stroke-width="2" fill="none"/>
      <rect x="162" y="40" width="430" height="9" rx="4" fill="#444"/>
      <rect x="162" y="40" width="215" height="9" rx="4" fill="var(--progress)"/>
      <path d="M786 32 h10 M786 32 v10 M786 32 l12 12 M812 56 h-10 M812 56 v-10 M812 56 l-12 -12" stroke="#fff" stroke-width="3" fill="none"/>
    </svg>
  </div>
</div>
<p class="abs copy" style="left:183px;top:2832px;width:834px;color:var(--ink)">Lorem ipsum dolor sit amet, consectetuer adipiscing elit, sed diam nonummy nibh euismod tincidunt ut laoreet dolore magna aliquam erat volutpat. Ut wisi enim ad minim veniam, quis nostrud exerci tation ullamcorper.</p>

<div class="abs player" style="left:163px;top:2903px;width:285px;height:194px;border-radius:3px">
  <div class="screen" style="height:168px;background:linear-gradient(180deg,#e0a461,#8a6a4a 60%,#3d4048)" role="img" aria-label="Video still of a drone lifting off at sunset"></div>
  <div class="play-big" style="left:122px;top:70px;width:40px;height:30px;border-radius:5px"><svg width="40" height="30"><polygon points="15,8 15,22 27,15" fill="#fff"/></svg></div>
  <div class="bar" style="height:26px"><svg width="285" height="26"><polygon points="10,7 10,19 19,13" fill="#fff"/><rect x="30" y="9" width="8" height="8" fill="#fff"/><rect x="50" y="11" width="150" height="4" rx="2" fill="#444"/><rect x="50" y="11" width="70" height="4" rx="2" fill="var(--progress)"/><rect x="262" y="8" width="10" height="10" fill="none" stroke="#fff" stroke-width="2"/></svg></div>
</div>
<div class="abs player" style="left:459px;top:2903px;width:282px;height:194px;border-radius:3px">
  <div class="screen" style="height:168px;background:linear-gradient(180deg,#f4f4f4,#d6d6d6)" role="img" aria-label="Video still of a fixed-wing mapping drone on a white background"></div>
  <div class="play-big" style="left:121px;top:70px;width:40px;height:30px;border-radius:5px"><svg width="40" height="30"><polygon points="15,8 15,22 27,15" fill="#fff"/></svg></div>
  <div class="bar" style="height:26px"><svg width="282" height="26"><polygon points="10,7 10,19 19,13" fill="#fff"/><rect x="30" y="9" width="8" height="8" fill="#fff"/><rect x="50" y="11" width="150" height="4" rx="2" fill="#444"/><rect x="50" y="11" width="70" height="4" rx="2" fill="var(--progress)"/><rect x="259" y="8" width="10" height="10" fill="none" stroke="#fff" stroke-width="2"/></svg></div>
</div>
<div class="abs player" style="left:752px;top:2903px;width:285px;height:194px;border-radius:3px">
  <div class="screen" style="height:168px;background:linear-gradient(180deg,#a7a39a,#6d6a66 60%,#4a4a4e)" role="img" aria-label="Video still of a crowd outside a stone building"></div>
  <div class="play-big" style="left:122px;top:70px;width:40px;height:30px;border-radius:5px"><svg width="40" height="30"><polygon points="15,8 15,22 27,15" fill="#fff"/></svg></div>
  <div class="bar" style="height:26px"><svg width="285" height="26"><polygon points="10,7 10,19 19,13" fill="#fff"/><rect x="30" y="9" width="8" height="8" fill="#fff"/><rect x="50" y="11" width="150" height="4" rx="2" fill="#444"/><rect x="50" y="11" width="70" height="4" rx="2" fill="var(--progress)"/><rect x="262" y="8" width="10" height="10" fill="none" stroke="#fff" stroke-width="2"/></svg></div>
</div>
<p class="abs thumb-caption" style="left:163px;top:3106px;width:285px">Lorem ipsum dolor sit amet, consectetuer adipiscing elit, sed diam nonummy nibh euismod.</p>
<p class="abs thumb-caption" style="left:459px;top:3106px;width:282px">Lorem ipsum dolor sit amet, consectetuer adipiscing elit, sed diam nonummy nibh euismod.</p>
<p class="abs thumb-caption" style="left:752px;top:3106px;width:285px">Lorem ipsum dolor sit amet, consectetuer adipiscing elit, sed diam nonummy nibh euismod.</p>

<!-- Pilots -->
<h2 class="abs section-title" style="top:3225px"><em>Our</em> Drone Pilots</h2>
<div class="abs title-rule" style="top:3279px"></div>

<div class="abs pilot-photo" style="left:171px;top:3318px;width:220px;height:220px" role="img" aria-label="Portrait of the owner and lead pilot"></div>
<div class="abs pilot-name" style="left:430px;top:3350px">Owen Marlow, <span>Owner / Pilot</span></div>
<p class="abs" style="left:430px;top:3378px;width:600px;font-size:12.5px;line-height:19px;color:var(--ink)">Lorem ipsum dolor sit amet, consectetuer adipiscing elit, sed diam nonummy nibh euismod tincidunt ut laoreet dolore magna aliquam erat volutpat. Ut wisi enim ad minim veniam, quis nostrud exerci tation ullamcorper suscipit lobortis nisl ut aliquip ex ea commodo consequat. Duis autem vel eum iriure dolor in hendrerit in vulputate velit esse molestie consequat, vel illum dolore eu feugiat nulla facilisis at vero eros et accumsan et iusto odio dignissim qui blandit praesent luptatum zzril delenit augue duis dolore te feugait nulla facilisi.</p>

<div class="abs avatar" style="left:343px;top:3508px" role="img" aria-label="Portrait of Owen Marlow"></div>
<div class="abs avatar" style="left:462px;top:3508px" role="img" aria-label="Portrait of Tobias Reed"></div>
<div class="abs avatar" style="left:581px;top:3508px" role="img" aria-label="Portrait of Felix Varga"></div>
<div class="abs avatar" style="left:702px;top:3508px" role="img" aria-label="Portrait of Cal Dunmore"></div>
<div class="abs avatar" style="left:824px;top:3508px" role="img" aria-label="Portrait of Ines Aldana"></div>
<div class="abs avatar-label" style="left:324px;top:3588px">Owen Marlow<br>Owner / Pilot</div>
<div class="abs avatar-label" style="left:443px;top:3588px">Tobias Reed</div>
<div class="abs avatar-label" style="left:562px;top:3588px">Felix Varga</div>
<div class="abs avatar-label" style="left:683px;top:3588px">Cal Dunmore</div>
<div class="abs avatar-label" style="left:805px;top:3588px">Ines Aldana,<br>CPA/CA</div>

<!-- CTA -->
<section class="abs cta"></section>
<div class="abs cta-text">Have questions about drone services?</div>
<div class="abs btn-dark">ASK NOW</div>

<!-- Footer -->
<footer class="abs site-footer"></footer>
<div class="abs inquiry-panel"></div>
<div class="abs footer-title large" style="left:191px;top:3840px">Quick Inquiry</div>
<div class="abs field" style="top:3884px">Name</div>
<div class="abs field" style="top:3920px">Phone</div>
<div class="abs field" style="top:3956px">Email</div>
<div class="abs field" style="top:3992px;height:76px;line-height:22px">Message</div>
<div class="abs btn-submit">Submit</div>

<div class="abs footer-title" style="left:500px;top:3848px">Quick links</div>
<div class="abs footer-rule" style="left:500px;top:3878px;width:110px"></div>
<div class="abs links">Home<br>About Us<br>Our Services<br>Pricing<br>Contact Us</div>

<div class="abs footer-title" style="left:658px;top:3848px">Contact Details</div>
<div class="abs footer-rule" style="left:658px;top:3878px;width:380px"></div>
<svg class="abs" style="left:655px;top:3904px" width="14" height="18"><path d="M7 1a5.5 5.5 0 0 0-5.5 5.5C1.5 11 7 17 7 17s5.5-6 5.5-10.5A5.5 5.5 0 0 0 7 1z" fill="#fff"/><circle cx="7" cy="6.5" r="2" fill="#3b3b3b"/></svg>
<div class="abs contact-line" style="left:680px;top:3903px"><strong>RM Skyline Imaging</strong><br>Street Name, City Name<br>State Zipcode</div>
<svg class="abs" style="left:878px;top:3906px" width="16" height="12"><rect x="0.5" y="0.5" width="15" height="11" fill="#fff"/><path d="M1 1l7 6 7-6" stroke="#3b3b3b" fill="none"/></svg>
<div class="abs contact-line" style="left:908px;top:3903px">inquiry@rmskylineimages.com</div>
<svg class="abs" style="left:878px;top:3940px" width="16" height="16"><circle cx="8" cy="8" r="8" fill="#fff"/><path d="M5 4l2 2-1 1.5c.8 1.5 1.8 2.5 3 3L10.5 9l2 2-1.5 1.5C8 12 4.5 8.5 4 5z" fill="#3b3b3b"/></svg>
<div class="abs contact-line" style="left:908px;top:3940px">123-456-7890</div>

<div class="abs footer-brand">RM Skyline Imaging</div>
<div class="abs copyright">Copyright © 2017 RM Skyline Imaging. All Rights Reserved</div>

</body>
</html>
```